Brindlecote Development Partners Web Site

We need a website design for a new land purchasing and development business based in PEI. We are just regular guys trying a new adventure buying small parcels of land, doing the hard work seperating them into lots, building roads and selling off a dream location. We help folks like ourselves buy the lots, create a house plan and help get the project done.

We have a wordpress website, but no skills. The site should have our simple story and links to individual land development progects, currently we have 2. The larger project is on a golf course and images have been uploaded. We would like a map of the properities with locations on the properties you can click to see the views/ pictures. It would be great to have the ability to superimpose house images on the lot images. This would help prospects see the end results. I have attached some photos and logo's, however, they are not manditory.
The project would have to allow for us to update and maintain the site.

Target Market(s)

Visitors to PEI, typically from larger cities in Ontario and Maine. Golfers that want to live on a golf course.

Industry/Entity Type

Realestate (land development)

Coding

Coded - Design and coding required

Number of Pages Required

4 page

Requirements
Must have
• Allow fo us to maintain the site. Company overview page with story and contact information. Links to current realestate projects (developments). Project pages with the informaiton on the land and purchasing. Since this is land not houses, maps to the site, maps of the parcel, maps of the individual lots with the ability to review photos based on the views of that particular lot.
Nice to have
• The ability to upload and overlay a house picture on the lot. This would provide a visual of the final build.

```html
<!DOCTYPE html>
<html lang="en">
<head>
<meta charset="utf-8">
<title>Brindlecote Development Partners</title>
<link rel="stylesheet" href="https://fonts.googleapis.com/css2?family=Montserrat:wght@300;400;500;600&family=Playfair+Display:wght@700&display=swap">
<style>
:root{
  --ink:#1c1c1c;
  --dark:#222222;
  --text:#444444;
  --muted:#666666;
  --white:#ffffff;
  --panel:#eeeeee;
  --soft:#f6f6f6;
  --btn:#9a9a9a;
  --rule:#9a9a9a;
}
*{margin:0;padding:0;box-sizing:border-box}
html,body{width:1200px;height:3162px;overflow:hidden}
body{position:relative;background:var(--white);font-family:"Montserrat",sans-serif;color:var(--text)}
.abs{position:absolute}
.serif{font-family:"Playfair Display",serif;font-weight:700;color:var(--ink)}

/* header */
.site-header{left:0;top:0;width:1200px;height:110px;background:var(--dark)}
.brand-tab{left:131px;top:0;width:262px;height:133px}
.brand-tab svg{position:absolute;left:0;top:0}
.brand-name{position:absolute;left:0;top:44px;width:262px;text-align:center;font-weight:600;font-size:20px;color:var(--ink)}
.brand-sub{position:absolute;left:0;top:70px;width:262px;text-align:center;font-size:11px;font-weight:600;color:var(--ink)}
.top-social{left:774px;top:22px;display:flex;gap:16px}
.dot-icon{width:14px;height:14px;border-radius:50%;background:var(--white)}
.top-phone{left:896px;top:19px;color:var(--white);font-size:17px;display:flex;align-items:center;gap:8px}
.top-phone .ph{width:20px;height:18px;background:#999;border-radius:3px;display:flex;align-items:center;justify-content:center}
.top-rule{left:567px;top:55px;width:633px;height:1px;background:#555}
.main-nav{left:0;top:66px}
.main-nav a{position:absolute;top:0;height:29px;line-height:29px;color:var(--white);text-decoration:none;font-size:16px;white-space:nowrap}
.main-nav a.active{background:#8d8d8d;width:85px;text-align:center}

/* hero */
.hero{left:0;top:110px;width:1200px;height:570px;background:linear-gradient(180deg,#7d9a74 0%,#55704a 25%,#3f5233 55%,#4a4a2e 80%,#2e3426 100%)}
.hero-text{left:0;top:235px;width:1200px;text-align:center}
.hero-welcome{font-size:32px;line-height:40px}
.hero-title{font-size:70px;line-height:66px}
.hero-partners{font-size:42px;line-height:50px}
.hero-text .serif{color:var(--white)}
.hero-copy{left:380px;top:390px;width:440px;text-align:center;color:#eee;font-size:13.5px;line-height:27px;font-weight:300}
.btn{position:absolute;background:var(--btn);color:#eee;font-size:14px;text-align:center;border-radius:4px;font-weight:400}

/* headings */
.sec-head{text-align:center;font-size:34px;line-height:44px}
.sec-rule{height:1px;background:var(--rule)}
.sec-rule::after{content:"";position:absolute;top:-2px;width:5px;height:5px;border-radius:50%;background:var(--ink);left:calc(50% - 2px)}
.lead{text-align:center;font-size:15px;line-height:27px;font-weight:300;color:var(--text);letter-spacing:-0.2px}

/* overview */
.overview-disc{left:31px;top:679px;width:466px;height:466px;border-radius:50%;background:var(--soft)}
.overview-mark{left:31px;top:960px;width:466px;text-align:center;font-weight:600;font-size:34px;color:var(--ink)}
.overview-mark small{display:block;font-size:15px;font-weight:500;margin-top:4px}
.overview-body{left:436px;top:837px;width:620px;font-size:14.5px;line-height:27.3px;font-weight:300;text-align:justify;letter-spacing:-0.2px}

/* projects */
.arrow-btn{width:46px;height:40px;border-radius:4px;display:flex;align-items:center;justify-content:center}
.arrow-prev{left:938px;top:1395px;background:#8f8f8f}
.arrow-next{left:1001px;top:1395px;background:var(--white);border:1px solid #ddd}
.card-photo{width:295px;height:274px;top:1453px}
.card-body{width:295px;height:117px;top:1745px;background:var(--panel);padding:13px 13px}
.card-body h3{font-size:17px;font-weight:600;color:var(--ink);margin-bottom:4px;line-height:22px}
.card-body p{font-size:13.5px;line-height:21px;font-weight:300;color:var(--muted);letter-spacing:-0.3px}

/* contact */
.contact-band{left:0;top:2140px;width:600px;height:552px;background:var(--dark)}
.contact-map{left:600px;top:2140px;width:600px;height:552px;background:linear-gradient(135deg,#f3f3f3,#e6e6e6 60%,#f0e4e4)}
.icon-ring{width:64px;height:64px;border:2px solid var(--white);border-radius:50%;display:flex;align-items:center;justify-content:center}
.c-label{color:var(--white);font-size:16px;text-align:center;width:260px}
.c-text{color:var(--white);font-size:12.5px;line-height:23px;text-align:center;width:260px}
.c-social{display:flex;gap:14px}
.c-social .dot-icon{width:13px;height:13px}

/* footer */
.site-footer{left:0;top:2820px;width:1200px;height:342px;background:var(--dark)}
.foot-tab{left:469px;top:2785px;width:263px;height:109px}
.foot-tab svg{position:absolute;left:0;top:0}
.foot-name{position:absolute;left:0;top:30px;width:263px;text-align:center;font-weight:600;font-size:20px;color:var(--ink)}
.foot-sub{position:absolute;left:0;top:56px;width:263px;text-align:center;font-size:11px;font-weight:600;color:var(--ink)}
.foot-copy{left:140px;top:2916px;width:920px;text-align:center;color:#ddd;font-size:15px;line-height:27px;font-weight:300;letter-spacing:-0.2px}
.foot-nav a{position:absolute;top:2993px;color:#ddd;font-size:16px;text-decoration:none}
.follow{left:517px;top:3037px;color:var(--white);font-size:15px;font-weight:600;display:flex;align-items:center;gap:12px}
.foot-rule{left:0;top:3079px;width:1200px;height:1px;background:#555}
.legal{left:0;top:3092px;width:1200px;text-align:center;color:#ddd;font-size:12.5px;font-weight:500}
</style>
</head>
<body>

<header class="abs site-header"></header>
<div class="abs brand-tab">
  <svg width="262" height="133" viewBox="0 0 262 133"><path d="M0 0H262V133Q131 100 0 133Z" fill="#ffffff"/></svg>
  <div class="brand-name">Brindlecote</div>
  <div class="brand-sub">Development Partners</div>
</div>
<div class="abs top-social"><span class="dot-icon"></span><span class="dot-icon"></span><span class="dot-icon"></span></div>
<div class="abs top-phone"><span class="ph"><svg width="11" height="11" viewBox="0 0 24 24"><path d="M6.6 10.8a15 15 0 006.6 6.6l2.2-2.2a1 1 0 011-.25 11 11 0 003.5.56 1 1 0 011 1V20a1 1 0 01-1 1A17 17 0 013 4a1 1 0 011-1h3.5a1 1 0 011 1c0 1.25.2 2.45.57 3.57a1 1 0 01-.25 1z" fill="#fff"/></svg></span>+1 5550 123 456</div>
<div class="abs top-rule"></div>
<nav class="abs main-nav">
  <a class="active" style="left:590px">Home</a>
  <a style="left:700px">About</a>
  <a style="left:790px">Services</a>
  <a style="left:895px">Projects</a>
  <a style="left:998px">Contact</a>
</nav>

<section class="abs hero" role="img" aria-label="Photo of a grassy Prince Edward Island field at dusk with a road curving through"></section>
<div class="abs hero-text">
  <div class="serif hero-welcome">Welcome to</div>
  <div class="serif hero-title">Brindlecote Development</div>
  <div class="serif hero-partners">Partners</div>
</div>
<p class="abs hero-copy">Lorem ipsum dolor sit amet, consectetur adipiscing elit, sed do eiusmod tempor incididunt ut labore et dolore magna aliqua.</p>
<a class="btn" style="left:519px;top:462px;width:161px;height:38px;line-height:38px">Get Started</a>

<div class="abs overview-disc"></div>
<div class="abs overview-mark">Brindlecote<small>Development Partners</small></div>
<h2 class="abs serif" style="left:434px;top:768px;font-size:34px;line-height:44px">Company Overview</h2>
<div class="abs sec-rule" style="left:434px;top:817px;width:266px"></div>
<p class="abs overview-body">Lorem ipsum dolor sit amet, consectetur adipiscing elit, sed do eiusmod tempor incididunt ut labore et dolore magna aliqua. Quis ipsum suspendisse ultrices gravida. Risus commodo viverra maecenas accumsan lacus vel facilisis. Lorem ipsum dolor sit amet, consectetur adipiscing elit, sed do eiusmod tempor incididunt ut labore et dolore magna aliqua. Quis ipsum suspendisse ultrices gravida. Risus commodo viverra maecenas accumsan lacus vel facilisis. sed do eiusmod tempor incididunt ut labore et dolore magna aliqua. Quis ipsum suspendisse ultrices gravida.</p>
<a class="btn" style="left:436px;top:1051px;width:162px;height:39px;line-height:39px">Read More</a>

<h2 class="abs serif sec-head" style="left:0;top:1228px;width:1200px">Our Latest Projects</h2>
<div class="abs sec-rule" style="left:436px;top:1281px;width:328px"></div>
<p class="abs lead" style="left:130px;top:1300px;width:940px">Lorem ipsum dolor sit amet, consectetur adipiscing elit, sed do eiusmod tempor incididunt ut labore et dolore magna aliqua. Quis ipsum suspendisse ultrices gravida. Risus commodo viverra maecenas accumsan lacus vel facilisis.</p>
<div class="abs arrow-btn arrow-prev"><svg width="14" height="16" viewBox="0 0 14 16"><path d="M10 2L4 8l6 6" stroke="#111" stroke-width="2.2" fill="none"/></svg></div>
<div class="abs arrow-btn arrow-next"><svg width="14" height="16" viewBox="0 0 14 16"><path d="M4 2l6 6-6 6" stroke="#111" stroke-width="2.2" fill="none"/></svg></div>

<div class="abs card-photo" style="left:146px;background:linear-gradient(180deg,#b9cde0 0%,#e8d3bd 30%,#3d5133 45%,#7c7a4f 75%,#9c8f6a 100%)" role="img" aria-label="Photo of a meadow with a line of evergreen trees"></div>
<div class="abs card-photo" style="left:453px;background:linear-gradient(180deg,#a9bfd1 0%,#d9d6cb 45%,#3e5035 58%,#6f7a52 75%,#7c7d78 100%)" role="img" aria-label="Photo of a paved path beside a grassy field"></div>
<div class="abs card-photo" style="left:760px;background:linear-gradient(180deg,#aac3df 0%,#e6d2c3 38%,#46573a 50%,#767550 75%,#948a62 100%)" role="img" aria-label="Photo of an open field with trees on the horizon"></div>

<div class="abs card-body" style="left:146px"><h3>Heading 1</h3><p>Lorem ipsum dolor sit amet, consectetur adipiscing elit, sed do eiusmod tempor incididunt ut labore et.</p></div>
<div class="abs card-body" style="left:453px"><h3>Heading 1</h3><p>Lorem ipsum dolor sit amet, consectetur adipiscing elit, sed do eiusmod tempor incididunt ut labore et.</p></div>
<div class="abs card-body" style="left:760px"><h3>Heading 1</h3><p>Lorem ipsum dolor sit amet, consectetur adipiscing elit, sed do eiusmod tempor incididunt ut labore et.</p></div>

<h2 class="abs serif sec-head" style="left:0;top:1969px;width:1200px">Contact Infomation</h2>
<div class="abs sec-rule" style="left:436px;top:2020px;width:328px"></div>
<p class="abs lead" style="left:160px;top:2040px;width:880px">Lorem ipsum dolor sit amet, consectetur adipiscing elit, sed do eiusmod tempor incididunt ut labore et dolore magna aliqua. Quis ipsum suspendisse ultrices gravida.</p>

<section class="abs contact-band"></section>
<div class="abs contact-map" role="img" aria-label="Site plan map of the development showing numbered lots and view directions"></div>

<div class="abs icon-ring" style="left:203px;top:2224px"><svg width="20" height="26" viewBox="0 0 20 26"><path d="M10 1a8 8 0 00-8 8c0 6 8 16 8 16s8-10 8-16a8 8 0 00-8-8zm0 11a3 3 0 110-6 3 3 0 010 6z" fill="#fff"/></svg></div>
<div class="abs c-label" style="left:105px;top:2310px">Address:</div>
<div class="abs c-text" style="left:105px;top:2342px">#1, Harbour Lane, Cove City,<br>PE -C0A 1B0.</div>

<div class="abs icon-ring" style="left:421px;top:2224px"><svg width="24" height="18" viewBox="0 0 24 18"><rect x="1" y="1" width="22" height="16" rx="2" fill="#fff"/><path d="M2 3l10 7 10-7" stroke="#222" stroke-width="2" fill="none"/></svg></div>
<div class="abs c-label" style="left:323px;top:2310px">Email:</div>
<div class="abs c-text" style="left:323px;top:2346px">info@brindlecote.example</div>

<div class="abs icon-ring" style="left:203px;top:2464px"><svg width="22" height="22" viewBox="0 0 24 24"><path d="M6.6 10.8a15 15 0 006.6 6.6l2.2-2.2a1 1 0 011-.25 11 11 0 003.5.56 1 1 0 011 1V20a1 1 0 01-1 1A17 17 0 013 4a1 1 0 011-1h3.5a1 1 0 011 1c0 1.25.2 2.45.57 3.57a1 1 0 01-.25 1z" fill="#fff"/></svg></div>
<div class="abs c-label" style="left:108px;top:2546px">Call Us:</div>
<div class="abs c-text" style="left:108px;top:2584px">+(1) 555 012 3456</div>

<div class="abs c-label" style="left:323px;top:2461px">Contact us:</div>
<div class="abs c-text" style="left:323px;top:2493px">Lorem ipsum dolor sit amet,<br>consectetur adipiscing elit, sed</div>
<div class="abs c-social" style="left:408px;top:2582px"><span class="dot-icon"></span><span class="dot-icon"></span><span class="dot-icon"></span></div>

<footer class="abs site-footer"></footer>
<div class="abs foot-tab">
  <svg width="263" height="109" viewBox="0 0 263 109"><path d="M0 0H263V109Q131 80 0 109Z" fill="#ffffff"/></svg>
  <div class="foot-name">Brindlecote</div>
  <div class="foot-sub">Development Partners</div>
</div>
<p class="abs foot-copy">Lorem Ipsum is simply dummy text of the printing and typesetting industry. Lorem Ipsum has been the industry's standard dummy text ever since the 1500s</p>
<nav class="foot-nav">
  <a class="abs" style="left:377px">Home</a>
  <a class="abs" style="left:467px">About</a>
  <a class="abs" style="left:556px">Services</a>
  <a class="abs" style="left:661px">Projects</a>
  <a class="abs" style="left:764px">Contact</a>
</nav>
<div class="abs follow">Follow us : <span class="dot-icon"></span><span class="dot-icon"></span><span class="dot-icon"></span></div>
<div class="abs foot-rule"></div>
<div class="abs legal">© copyrights 2022 Brindlecote Development Partners | All Rights Reserved</div>

</body>
</html>
```